Software - upgrade look and feel

Brightmile Ledgerworks is the worldwide distributor of the uPlotta software application, which powers a loan strategy as described at www.brightmileledgerworks.com.The company has recently upgraded its image and website; and now seeks to give uPlotta a much-needed face-lift.Using the screen shots of the existing application (2 x screens provided), recreate the screens in a modern and vibrant style that generates a feeling of professionalism and confidence.
Updates

Project not yet launched and I felt 5 days was inadequate.

Target Market(s)

Financial services industry and their clients.

Industry/Entity Type

Financial Service

Font styles to use
Other font styles liked:
• See our website at brightmileledgerworks.com - happy with this font, but open to ideas.

Colors

Designer to choose colors to be used in the design.

Requirements
Must have
• Existing fields, but perhaps more intuitive for the User.
Nice to have
• A less busy look that suggests an innovative software application.
Should not have
• Complication.

```html
<!DOCTYPE html>
<html lang="en">
<head>
<meta charset="utf-8">
<title>uPlotta – Client</title>
<link href="https://fonts.googleapis.com/css2?family=Questrial&family=Montserrat:wght@700&display=swap" rel="stylesheet">
<style>
:root{
  --teal:#1b9bb3;
  --navy:#2c3e50;
  --header:#2e3d4f;
  --page:#ebebeb;
  --panel:#ffffff;
  --field:#ebebeb;
  --ink:#1c1c1c;
  --tab:rgba(255,255,255,.38);
  --tab-active:#82c0cb;
}
*{box-sizing:border-box;margin:0;padding:0}
html,body{width:1200px;height:753px;overflow:hidden;background:var(--page)}
body{position:relative;font-family:"Questrial",sans-serif;color:var(--ink);font-size:15px}
.abs{position:absolute}
.sidebar{left:0;top:0;width:211px;height:753px;background:linear-gradient(180deg,var(--teal) 0%,#217f97 30%,#2a5468 60%,var(--navy) 100%)}
.brand{left:8px;top:60px;display:flex;align-items:center;gap:12px}
.brand-mark{width:60px;height:60px;background:rgba(255,255,255,.55)}
.brand-name{font-size:30px;color:rgba(255,255,255,.75)}
.steps{left:0;top:0;width:260px;height:753px}
.step{color:#fff;line-height:1}
.step .num{font-size:30px}
.step .sub{font-size:17px;position:absolute;right:0;white-space:nowrap}
.rights{left:24px;top:727px;color:#fff;font-size:16px}
.topbar{left:211px;top:6px;width:989px;height:45px;background:var(--header);color:#fff;display:flex;justify-content:space-between;align-items:center;padding:0 18px;font-size:30px}
.panel{background:var(--panel)}
.label{white-space:nowrap;line-height:1}
.field{background:var(--field);border-radius:9px;height:18px}
.select::after{content:"";position:absolute;right:10px;top:6px;border-left:5px solid transparent;border-right:5px solid transparent;border-top:7px solid #111}
.link{text-decoration:underline;text-underline-offset:3px}
.notice{font-family:"Montserrat",sans-serif;font-weight:700;font-size:15.5px;line-height:33px;width:940px}
.total-label{font-size:18px}
.total-box{background:var(--field);border-radius:8px}
.btn{background:var(--field);border-radius:9px;height:21px;display:flex;align-items:center;justify-content:center;font-size:17px}
</style>
</head>
<body>
<aside class="abs sidebar">
  <div class="abs brand"><span class="brand-mark"></span><span class="brand-name">Brightmile</span></div>
  <div class="abs rights">all rights reserved</div>
</aside>
<svg class="abs steps" viewBox="0 0 260 753" aria-hidden="true">
  <polygon points="2,171 211,171 248,207 211,242 2,242" fill="var(--tab-active)"/>
  <polygon points="2,246 177,246 211,276 177,306 2,306" fill="var(--tab)"/>
  <polygon points="2,310 177,310 211,340 177,371 2,371" fill="var(--tab)"/>
  <polygon points="2,374 177,374 211,405 177,436 2,436" fill="var(--tab)"/>
  <polygon points="2,438 177,438 211,469 177,500 2,500" fill="var(--tab)"/>
</svg>
<nav>
  <div class="abs step" style="left:8px;top:175px;width:193px;height:64px"><span class="num" style="font-size:36px">Step 1</span><span class="sub" style="top:43px;font-size:20px">Client/Income</span></div>
  <div class="abs step" style="left:8px;top:252px;width:163px;height:52px"><span class="num">Step 2</span><span class="sub" style="top:32px">Expenses</span></div>
  <div class="abs step" style="left:8px;top:317px;width:165px;height:52px"><span class="num">Step 3</span><span class="sub" style="top:33px">Assets/Liabilities</span></div>
  <div class="abs step" style="left:8px;top:380px;width:166px;height:52px"><span class="num">Step 4</span><span class="sub" style="top:34px">Restructure</span></div>
  <div class="abs step" style="left:8px;top:444px;width:166px;height:52px"><span class="num">Step 5</span><span class="sub" style="top:35px">Calculate</span></div>
</nav>

<header class="abs topbar"><span>Client</span><span>Ada &amp; Tom Reyes</span></header>

<section class="abs panel" style="left:221px;top:59px;width:968px;height:158px"></section>
<div class="abs label" style="left:725px;top:78px;font-size:10px">Additional Details</div>
<div class="abs label" style="left:244px;top:93px">View</div>
<div class="abs label" style="left:244px;top:125px">Loan Writer User</div>
<div class="abs label" style="left:244px;top:159px">CS Officer</div>
<div class="abs field select" style="left:372px;top:92px;width:156px"></div>
<div class="abs field select" style="left:372px;top:124px;width:156px"></div>
<div class="abs field select" style="left:372px;top:157px;width:156px"></div>
<div class="abs label" style="left:561px;top:93px">Title</div>
<div class="abs label" style="left:560px;top:125px">Family Name</div>
<div class="abs label" style="left:561px;top:159px">First Name</div>
<div class="abs field" style="left:662px;top:92px;width:156px"></div>
<div class="abs field" style="left:662px;top:124px;width:156px"></div>
<div class="abs field" style="left:662px;top:157px;width:156px"></div>
<div class="abs label" style="left:860px;top:93px">File No</div>
<div class="abs label" style="left:859px;top:126px">Email</div>
<div class="abs label" style="left:858px;top:159px">Statistics</div>
<div class="abs field" style="left:981px;top:92px;width:157px"></div>
<div class="abs field" style="left:981px;top:124px;width:157px"></div>
<div class="abs label" style="left:979px;top:159px">Send to Pending Tray</div>

<section class="abs panel" style="left:221px;top:248px;width:968px;height:390px"></section>
<div class="abs label" style="left:330px;top:269px">Simulation Purpose</div>
<div class="abs field select" style="left:506px;top:268px;width:156px"></div>
<div class="abs label link" style="left:754px;top:269px">Minimization Strategy</div>
<div class="abs label link" style="left:958px;top:269px">NLBA Guidelines</div>
<p class="abs notice" style="left:238px;top:298px">Please enter the Names of Client 1 and Client 2,(if applicable), then enter after tax, wage or salary per frequency of payment</p>
<div class="abs label" style="left:400px;top:361px">Net (after tax)</div>
<div class="abs label" style="left:578px;top:361px">Freq of Payment</div>
<div class="abs label" style="left:252px;top:391px">Client 1</div>
<div class="abs label" style="left:252px;top:423px">Client 2</div>
<div class="abs field" style="left:372px;top:390px;width:156px"></div>
<div class="abs field" style="left:565px;top:390px;width:157px"></div>
<div class="abs field" style="left:372px;top:420px;width:156px"></div>
<div class="abs field" style="left:565px;top:420px;width:157px"></div>
<p class="abs notice" style="left:238px;top:459px">Note: Unless you enter the name of Client 1, no income will be saved for Client 1.Unless you enter the name of Client 2, no income may be entered for Client 2</p>
<div class="abs label total-label" style="left:674px;top:532px">Client 1 After Tax Income</div>
<div class="abs label total-label" style="left:673px;top:575px">Combined After Tax Income</div>
<div class="abs total-box" style="left:934px;top:522px;width:239px;height:36px"></div>
<div class="abs total-box" style="left:934px;top:564px;width:239px;height:35px"></div>

<section class="abs panel" style="left:221px;top:666px;width:968px;height:57px"></section>
<div class="abs label" style="left:596px;top:687px;font-size:16px">Total are updated by clicking save</div>
<div class="abs btn" style="left:899px;top:685px;width:80px">Save</div>
<div class="abs btn" style="left:1006px;top:685px;width:80px">Cancel</div>
</body>
</html>
```